DRAINWELL HOT WATER CYLINDER STICKER – PRINT LAYOUT

SECTION 1 – HOMEOWNER MAINTENANCE GUIDE (Boxed Section):
πŸ“– Hot Water Cylinder Maintenance
βœ… Monthly: Quick visual check for leaks, rust, or pooling water.
βœ… Every 6 Months: Test your TPR (Temperature & Pressure Relief) valve.
β€’ Lift the lever gently until water flows, then release.
β€’ If it’s blocked or constantly dripping – call us immediately.
βœ… Listen: Popping, banging, or rumbling? Could be sediment build-up.
βœ… Annually: Book a professional service to check anode, thermostat & valves.

SECTION 2 – WARNING SIGNS (Highlight Box or Red Accent):
🚨 Call Us Immediately If You Notice:
β€’ No hot water or inconsistent temperature
β€’ Water leaking from tank or pipes
β€’ Rust-coloured water
β€’ Sudden drop in water pressure

SECTION 3 – CALL TO ACTION (Large & Bold):
πŸ“ž NEED HELP FAST? CALL DRAINWELL FIRST!
πŸ“² PHONE: [0431 258 907] (largest text on sticker)
🌐 [www.drainwell.com.au]

FOOTER (Small Print):
Fully Licensed & Insured | HKTR 62840315 | 24/7 Emergency Service
This guide is for general maintenance only. For all repairs or safety concerns, contact a licensed plumber.

βœ… DESIGN RECOMMENDATIONS
β€’ Size: 27cm long x 10cm wide works well (large enough to read easily when standing).
β€’ Material: Waterproof vinyl with strong adhesive.
β€’ Colors:
o Header & Call-to-Action in your brand colors
o Maintenance guide in a light-shaded box for contrast
o Warning signs section with red accent or icon to grab attention
β€’ Icons: Use βœ… πŸ“– 🚨 πŸ“ž for quick scanning.

```html
<!DOCTYPE html>
<html lang="en">
<head>
<meta charset="utf-8">
<title>Drainwell – Hot Water Cylinder Maintenance Sticker</title>
<link rel="stylesheet" href="https://fonts.googleapis.com/css2?family=Heebo:wght@400;500;700;800&display=swap">
<style>
  :root {
    --page-bg: #e6e8ea;
    --slate: #6b6b6e;
    --guide-bg: #c9d6df;
    --white: #ffffff;
    --ink: #1e1e20;
    --navy: #1b3555;
    --alert: #e4412b;
    --bullet-grey: #6b6b6e;
    --brand-blue: #1f73b7;
  }
  * { box-sizing: border-box; margin: 0; padding: 0; }
  html, body {
    width: 1200px; height: 675px; overflow: hidden;
    background: var(--page-bg);
    font-family: "Heebo", Arial, sans-serif;
  }
  .sticker {
    position: absolute; left: 202px; top: 28px;
    width: 795px; height: 619px;
    background: var(--white);
    overflow: hidden;
  }

  /* Header */
  .header { position: absolute; left: 0; top: 0; width: 100%; height: 86px; background: var(--slate); }
  .brand {
    position: absolute; left: 0; top: 0; width: 210px; height: 86px;
    background: var(--white);
    display: flex; flex-direction: column; justify-content: center; padding-left: 22px;
  }
  .brand-name { display: flex; align-items: center; gap: 7px; font-weight: 700; font-size: 20px; color: var(--brand-blue); letter-spacing: .3px; }
  .brand-dot { width: 16px; height: 16px; border-radius: 50%; background: var(--brand-blue); }
  .brand-tagline { margin-top: 2px; padding-left: 23px; font-size: 8.5px; color: var(--slate); letter-spacing: .2px; }
  .title {
    position: absolute; left: 237px; top: 0; height: 86px; line-height: 86px;
    font-size: 31px; font-weight: 700; color: var(--white); letter-spacing: .2px;
  }

  /* Maintenance guide */
  .guide { position: absolute; left: 0; top: 86px; width: 100%; height: 158px; background: var(--guide-bg); }
  .task { position: absolute; top: 17px; }
  .task-head { display: flex; align-items: center; gap: 8px; font-size: 21.5px; font-weight: 500; color: var(--ink); height: 24px; }
  .task-dot { width: 21px; height: 21px; border-radius: 50%; background: var(--bullet-grey); flex: none; }
  .task-line { position: relative; padding-left: 29px; margin-top: 4px; font-size: 13.6px; line-height: 17px; color: var(--ink); }
  .task-line + .task-line { margin-top: 0; }
  .tick { position: absolute; left: 1px; top: 1px; width: 19px; height: 15px; }
  .sub-dot { position: absolute; left: 7px; top: 5px; width: 7px; height: 7px; border-radius: 50%; background: var(--bullet-grey); }
  .sub-text { padding-left: 4px; }
  .task-monthly { left: 31px; width: 160px; }
  .task-six { left: 197px; width: 215px; }
  .task-listen { left: 423px; width: 160px; }
  .task-annual { left: 605px; width: 170px; }

  /* Warning signs */
  .warning-label {
    position: absolute; left: 64px; top: 250px; width: 180px; height: 32px;
    background: var(--alert); color: var(--white);
    font-size: 17px; font-weight: 700; letter-spacing: .6px;
    display: flex; align-items: center; justify-content: center;
  }
  .siren { position: absolute; left: 70px; top: 306px; width: 70px; height: 58px; }
  .warning-list { position: absolute; left: 155px; top: 288px; list-style: none; }
  .warning-list li {
    position: relative; padding-left: 20px;
    font-size: 19.5px; font-weight: 700; color: var(--navy); line-height: 24.5px;
  }
  .warning-list li::before {
    content: ""; position: absolute; left: 1px; top: 9px;
    width: 7px; height: 7px; border-radius: 50%; background: var(--alert);
  }
  .alert-rule { position: absolute; left: 79px; top: 403px; width: 633px; height: 3px; background: var(--alert); }

  /* Call to action */
  .cta { position: absolute; left: 0; top: 406px; width: 100%; height: 213px; background: var(--slate); color: var(--white); text-align: center; }
  .cta-lead { position: absolute; top: 22px; width: 100%; font-size: 21.5px; font-weight: 700; letter-spacing: .5px; }
  .cta-phone {
    position: absolute; top: 48px; width: 100%;
    display: flex; justify-content: center; align-items: center; gap: 12px;
    font-size: 60px; font-weight: 800; line-height: 72px; letter-spacing: 1px;
  }
  .phone-icon { width: 40px; height: 40px; margin-top: 6px; }
  .cta-web { position: absolute; top: 118px; width: 100%; font-size: 21px; font-weight: 700; }
  .credentials { position: absolute; top: 155px; width: 100%; font-size: 17px; font-weight: 500; }
  .disclaimer { position: absolute; top: 180px; width: 100%; font-size: 10.8px; font-weight: 500; }
</style>
</head>
<body>
<main class="sticker">
  <header class="header">
    <div class="brand">
      <div class="brand-name"><span class="brand-dot"></span>DRAINWELL</div>
      <div class="brand-tagline">PLUMBING | DRAINAGE | GAS</div>
    </div>
    <h1 class="title">Hot Water Cylinder Maintenance</h1>
  </header>

  <section class="guide">
    <div class="task task-monthly">
      <div class="task-head"><span class="task-dot"></span>Monthly</div>
      <p class="task-line"><svg class="tick" viewBox="0 0 19 15"><path d="M2 8 L7 13 L17 2" fill="none" stroke="#6b6b6e" stroke-width="3.4" stroke-linecap="round" stroke-linejoin="round"/></svg>Quick visual check for leaks, rust, or pooling water.</p>
    </div>
    <div class="task task-six">
      <div class="task-head"><span class="task-dot"></span>Every 6 Months</div>
      <p class="task-line"><svg class="tick" viewBox="0 0 19 15"><path d="M2 8 L7 13 L17 2" fill="none" stroke="#6b6b6e" stroke-width="3.4" stroke-linecap="round" stroke-linejoin="round"/></svg>Test your TPR (Temperature &amp; Pressure Relief) valve.</p>
      <p class="task-line"><span class="sub-dot"></span><span class="sub-text">Lift the lever gently until</span><br>water flows, then release.</p>
      <p class="task-line"><span class="sub-dot"></span><span class="sub-text">Lift the lever gently until</span><br>water flows, then release.</p>
    </div>
    <div class="task task-listen">
      <div class="task-head"><span class="task-dot"></span>Listen</div>
      <p class="task-line"><svg class="tick" viewBox="0 0 19 15"><path d="M2 8 L7 13 L17 2" fill="none" stroke="#6b6b6e" stroke-width="3.4" stroke-linecap="round" stroke-linejoin="round"/></svg>Popping, banging, or rumbling? Could be sediment build-up.</p>
    </div>
    <div class="task task-annual">
      <div class="task-head"><span class="task-dot"></span>Annually</div>
      <p class="task-line"><svg class="tick" viewBox="0 0 19 15"><path d="M2 8 L7 13 L17 2" fill="none" stroke="#6b6b6e" stroke-width="3.4" stroke-linecap="round" stroke-linejoin="round"/></svg>Book a professional service to check anode, thermostat &amp; valves.</p>
    </div>
  </section>

  <div class="warning-label">WARNING SIGNS</div>
  <svg class="siren" viewBox="0 0 70 58" aria-hidden="true">
    <g fill="none" stroke="#e4412b" stroke-width="3" stroke-linecap="round">
      <path d="M18 4 L23 10"/><path d="M52 4 L47 10"/>
      <path d="M6 16 L14 19"/><path d="M64 16 L56 19"/>
      <path d="M3 28 L12 28"/><path d="M67 28 L58 28"/>
    </g>
    <path d="M19 45 V30 A16 16 0 0 1 51 30 V45 Z" fill="#e4412b"/>
    <path d="M24 44 V31 A11 11 0 0 1 46 31 V44 Z" fill="#fff"/>
    <circle cx="35" cy="32" r="4.5" fill="#e4412b"/>
    <rect x="33" y="34" width="4" height="8" fill="#e4412b"/>
    <rect x="14" y="45" width="42" height="11" rx="1" fill="#e4412b"/>
    <rect x="27" y="49" width="16" height="3" fill="#fff"/>
  </svg>
  <ul class="warning-list">
    <li>No hot water</li>
    <li>Water leaking from tank or pipes</li>
    <li>Rust-cloloured water</li>
    <li>Sudden drop in water pressure</li>
  </ul>
  <div class="alert-rule"></div>

  <section class="cta">
    <p class="cta-lead">NEED HELP FAST? CALL DRAINWELL FIRST!</p>
    <p class="cta-phone">
      <svg class="phone-icon" viewBox="0 0 24 24" aria-hidden="true"><path fill="#fff" d="M6.6 10.8a15.1 15.1 0 0 0 6.6 6.6l2.2-2.2c.3-.3.7-.4 1-.2 1.1.4 2.3.6 3.6.6.6 0 1 .4 1 1V20c0 .6-.4 1-1 1A17 17 0 0 1 3 4c0-.6.4-1 1-1h3.5c.6 0 1 .4 1 1 0 1.3.2 2.5.6 3.6.1.3 0 .7-.2 1z"/></svg>
      0431 258 907
    </p>
    <p class="cta-web">www.drainwell.com.au</p>
    <p class="credentials">Fully Licensed &amp; Insured | HKTR 62840315 | 24/7 Emergency Service</p>
    <p class="disclaimer">This guide is for general maintenance only. For all repairs or safety concerns, contact a licensed plumber.</p>
  </section>
</main>
</body>
</html>
```